Copperfield Capital Partners Web Design

Copperfield Capital Partners is a national strategic business consulting company serving both marijuana businesses and investors. We assist emerging businesses in the marijuana sector that need assistance in developing their brand awareness and investor visibility within the industry. In addition, we provide information about these companies to investors so the can make financial decisions and discuss them in our forums. We would like to see designs that use the colors green, black and grey but please feel free to use your imagination. The final design should communicate financial growth

Target Market(s)

21-55+ men willing to invest in the marijuana market. These are savvy people who are expect to see a professional website.

Industry/Entity Type

Business

Coding

Coded - Design and coding required

Number of Pages Required

5+ page

Font styles to use
Serif
Sans Serif

Colors
abd036
cadf82
9bcb3c
c3c3c3
ffffff
000000

Requirements
Must have
• A Homepage, About Us page, Contact Us page, Watch List, Forums, a Disclaimer page, Privacy Policy and a "Watch List" page for us to promote marijuana companies on. We need a section to ask for visitor email addresses to join our mailing list. The site must be simple to navigate, but professional. If you were going to invest money into a risky marijuana market, what kind of website would you trust to get your information from?
Nice to have
• Our Facebook and Twitter integrated:
• www.facebook.com/CopperfieldCapitalPartners
• twitter.com/CopperfieldCP
• It would be nice if we could have a rolling comments section, where visitors can use facebook or whatever to post a quick comment. Maybe a testimonials page.
• It would be nice to have a blog page.

```html
<!DOCTYPE html>
<html lang="en">
<head>
<meta charset="utf-8">
<title>Copperfield Capital Partners</title>
<link rel="stylesheet" href="https://fonts.googleapis.com/css2?family=Yanone+Kaffeesatz:wght@300;400;600&family=Advent+Pro:wght@200&family=Lato:wght@300&display=swap">
<style>
:root{
  --ink:#000000;
  --white:#ffffff;
  --grey:#c3c3c3;
  --grey-text:#8a8a8a;
  --green:#9bcb3c;
  --green-soft:#abd036;
  --green-pale:#cadf82;
  --topbar:#0c0306;
  --base:#1b1e20;
  --logo-grey:#4a4a4a;
  --logo-green:#6a9c1c;
}
*{margin:0;padding:0;box-sizing:border-box}
html,body{width:1170px;height:1200px;overflow:hidden;background:var(--white)}
body{position:relative;font-family:"Yanone Kaffeesatz",sans-serif;color:var(--ink)}
.topbar{position:absolute;left:0;top:0;width:1170px;height:31px;background:var(--topbar);color:var(--white);font-size:12px;font-weight:600}
.topbar .contact{position:absolute;left:94px;top:8px;display:flex;gap:26px;align-items:center}
.topbar .contact span{display:flex;align-items:center;gap:6px}
.topbar .social{position:absolute;right:70px;top:8px;display:flex;gap:18px}
.topbar .social i{display:block;width:11px;height:11px;border-radius:50%;background:var(--white)}
.header{position:absolute;left:0;top:31px;width:1170px;height:105px;background:var(--white)}
.brand{display:flex;align-items:center;gap:14px}
.brand .mark{width:14px;height:14px;background:var(--green)}
.brand .name{font-weight:400;color:var(--green);letter-spacing:1px;text-transform:uppercase}
.header .brand{position:absolute;left:108px;top:38px}
.header .brand .name{font-size:28px}
.nav{position:absolute;right:86px;top:45px;display:flex;gap:25px;font-size:12px;font-weight:600;text-transform:uppercase}
.nav a{color:var(--ink);text-decoration:none;display:flex;align-items:center;gap:6px}
.hero{position:absolute;left:0;top:136px;width:1170px;height:580px;background:linear-gradient(100deg,#5a524d 0%,#b6b3ae 28%,#e9e9e7 48%,#cfcdca 62%,#4f5157 80%,#2c2e33 100%)}
.hero .photo{position:absolute;inset:0}
.hero .plate{position:absolute;left:172px;top:83px;width:828px;height:130px;background:rgba(200,200,200,.8);display:flex;justify-content:center;align-items:center}
.hero .plate .name{font-size:34px}
.hero .plate .mark{width:18px;height:18px}
.hero .tagline{position:absolute;left:0;width:1170px;top:231px;text-align:center;font-size:17px;font-weight:400}
.features{position:absolute;left:0;top:326px;width:1170px;height:206px;background:rgba(171,208,54,.8);display:flex;padding:0 80px}
.feature{flex:1;text-align:center;padding-top:26px}
.feature h3{font-size:17px;font-weight:600;margin:13px 0 22px}
.feature p{font-size:12px;line-height:16px}
.content{position:absolute;left:89px;top:770px;width:990px}
.content h1{font-family:"Advent Pro",sans-serif;font-weight:200;font-size:40px;color:#555}
.content p{font-family:"Lato",sans-serif;font-weight:300;font-size:13.5px;line-height:16.5px;color:var(--grey-text);margin-top:44px}
.cta{position:absolute;left:0;top:943px;width:1170px;height:194px;background:var(--green)}
.cta .mark{position:absolute;left:190px;top:98px;width:18px;height:18px;background:var(--logo-grey)}
.cta .divider{position:absolute;left:241px;top:52px;width:2px;height:110px;background:var(--logo-grey)}
.cta .name{position:absolute;left:270px;top:68px;font-size:32px;line-height:36px;color:var(--logo-green);letter-spacing:1px;text-transform:uppercase}
.cta p{position:absolute;left:595px;top:60px;width:470px;color:var(--white);font-size:12.5px;font-weight:600;line-height:17px}
.cta .mail{position:absolute;left:596px;top:127px;width:469px;height:35px;border:1px solid var(--white);color:var(--white);font-size:13px;display:flex;justify-content:center;align-items:center;gap:6px}
.base{position:absolute;left:0;top:1137px;width:1170px;height:63px;background:var(--base);color:var(--white)}
.base small{position:absolute;left:88px;top:24px;font-size:11px;font-weight:600}
.base .top{position:absolute;right:94px;top:24px}
</style>
</head>
<body>
<div class="topbar">
  <div class="contact">
    <span><svg width="10" height="10" viewBox="0 0 10 10"><path d="M2 1l2 2-1 1.2c.6 1.3 1.5 2.2 2.8 2.8L7 6l2 2-1.2 1.2C4.5 9 1 5.5.8 2.2z" fill="#fff"/></svg>+1 (555) 010-2398</span>
    <span><svg width="11" height="8" viewBox="0 0 11 8"><rect x=".5" y=".5" width="10" height="7" fill="none" stroke="#fff"/><path d="M.5.5l5 4 5-4" fill="none" stroke="#fff"/></svg>hello@copperfieldcp.example</span>
  </div>
  <div class="social" aria-label="Social links"><i></i><i></i><i></i><i></i></div>
</div>

<header class="header">
  <div class="brand"><span class="mark"></span><span class="name">Copperfield Capital Partners</span></div>
  <nav class="nav">
    <a href="#"><svg width="10" height="8" viewBox="0 0 10 8"><path d="M0 1h10M0 4h10M0 7h10" stroke="#000" stroke-width="1.5"/></svg>Home</a>
    <a href="#">Services</a>
    <a href="#">Watch List</a>
    <a href="#">About Us</a>
    <a href="#"><svg width="11" height="8" viewBox="0 0 11 8"><rect x=".5" y=".5" width="10" height="7" fill="none" stroke="#000"/><path d="M.5.5l5 4 5-4" fill="none" stroke="#000"/></svg>Contact</a>
  </nav>
</header>

<section class="hero">
  <div class="photo" role="img" aria-label="Blurred photo of business people reviewing financial charts on paper with a pen"></div>
  <div class="plate"><div class="brand"><span class="mark"></span><span class="name">Copperfield Capital Partners</span></div></div>
  <p class="tagline">Copperfield Capital Partners is a national strategic business consulting company serving both marijuana businesses and investors.</p>
  <div class="features">
    <div class="feature"><svg width="38" height="38" viewBox="0 0 38 38"><circle cx="19" cy="19" r="15" fill="none" stroke="#000" stroke-width="5"/><circle cx="19" cy="19" r="5.5" fill="#000"/></svg><h3>Lorem Ipsum</h3><p>Lorem ipsum, just the demo text for preview purpose.<br>Lorem ipsum, just the demo text for preview purpose.</p></div>
    <div class="feature"><svg width="38" height="38" viewBox="0 0 38 38"><circle cx="19" cy="19" r="15" fill="none" stroke="#000" stroke-width="5"/><circle cx="19" cy="19" r="5.5" fill="#000"/></svg><h3>Lorem Ipsum</h3><p>Lorem ipsum, just the demo text for preview purpose.<br>Lorem ipsum, just the demo text for preview purpose.</p></div>
    <div class="feature"><svg width="38" height="38" viewBox="0 0 38 38"><circle cx="19" cy="19" r="15" fill="none" stroke="#000" stroke-width="5"/><circle cx="19" cy="19" r="5.5" fill="#000"/></svg><h3>Lorem Ipsum</h3><p>Lorem ipsum, just the demo text for preview purpose.<br>Lorem ipsum, just the demo text for preview purpose.</p></div>
    <div class="feature"><svg width="38" height="38" viewBox="0 0 38 38"><circle cx="19" cy="19" r="15" fill="none" stroke="#000" stroke-width="5"/><circle cx="19" cy="19" r="5.5" fill="#000"/></svg><h3>Lorem Ipsum</h3><p>Lorem ipsum, just the demo text for preview purpose.<br>Lorem ipsum, just the demo text for preview purpose.</p></div>
  </div>
</section>

<main class="content">
  <h1>Content Goes Here..</h1>
  <p>Lorem ipsum as demo text filling this block for you to preview. Lorem ipsum as demo text filling this block for you to preview. Lorem ipsum as demo text filling this block for you to preview. Lorem ipsum as demo text filling this block for you to preview. Lorem ipsum as demo text filling this block for you to preview. Lorem ipsum as demo text filling this block for you to preview. Lorem ipsum as demo text filling this block for you to preview. Lorem ipsum as demo text filling this block for you to preview.</p>
</main>

<section class="cta">
  <span class="mark"></span>
  <span class="divider"></span>
  <span class="name">Copperfield<br>Capital Partners</span>
  <p>Lorem ipsum as demo text filling this block for you to preview. Lorem ipsum as demo text filling this block for you to preview. Lorem ipsum as demo text filling this block for you to preview. Lorem ipsum as demo text filling this block for you to preview. Lorem ipsum as demo text filling this block for you to preview. Lorem ipsum as demo text filling this block for you to preview. Lorem ipsum as demo text filling this block for you to preview.</p>
  <div class="mail"><svg width="11" height="11" viewBox="0 0 11 11"><path d="M10.5.5L.5 5l4 1.5L6 10.5z" fill="none" stroke="#fff"/><path d="M10.5.5L4.5 6.5" stroke="#fff"/></svg>hello@copperfieldcp.example</div>
</section>

<footer class="base">
  <small>Copyright ©2015 | Copperfield Capital Partners</small>
  <svg class="top" width="10" height="10" viewBox="0 0 10 10"><path d="M5 1v8M1.5 4.5L5 1l3.5 3.5" fill="none" stroke="#fff" stroke-width="1.6"/></svg>
</footer>
</body>
</html>
```